Certified Probate & Trust Postcard

Hi, I am looking for your assistance. I need a postcard design based on the following specifications. The postcard needs to be 6x9. Here are the specifications for the front and back sides. I also need help incorporating a section on the front of the postcard where I can write the name or names of the people I am addressing the postcard to, as well as a space on the back for the stamp and the receiver's address.

(revised 6/18/2025)
🖼️ FRONT SIDE

(Visual: A serene Bay Area home or warm, sunlit interior. Include Tessa’s headshot. Color palette: ivory, slate, soft gold.)

Headline:

You’ve Taken On So Much — Let Me Help with What Comes Next

Subhead:

Strategic Real Estate Guidance for Probate & Trust
Certified Probate & Trust Specialist | Serving the San Francisco Bay Area

⸻

đź“© BACK SIDE

Opening Quote (italicized):

“I lost both of my parents in 2020 — just weeks apart. That experience shaped how I serve every estate I touch.”

⸻

Main Body Copy:

My name is Tessa Varden, and I’m a Certified Probate & Trust Specialist who works with families, attorneys, and fiduciaries to guide the real estate side of probate with structure, sensitivity, and strategy.

Whether you’re navigating this with legal support or filing in pro per, this process is layered — emotional, procedural, and often overwhelming. I provide a steady hand when everything else feels uncertain.

With over a decade of experience supporting executives at Corvane, Lumirel, and Dunmore Pike, I bring the same operational precision and discretion to every estate I manage. But I also bring empathy — because I’ve been in your shoes.

⸻

What I Offer — At No Upfront Cost to the Estate:
• Property clean-outs, inspections, and basic preparation — coordinated and covered
• Real estate strategy aligned with court timelines and estate goals
• Hands-on collaboration with attorneys or step-by-step guidance for independent petitioners
• Thoughtful communication that honors your time and your grief

Because real estate isn’t just business.
For you, it’s personal. For me, it’s both.

⸻

Call to Action (in soft gold frame or slate border):

If you’re managing a probate or trust estate and need support you can trust — let’s make this easier, together.
Instagram: @itstessavoo | LinkedIn: profilehub.net/in/tessahomesagent

Industry/Entity Type

Real Estate

Requirements
Must have
• Image needs to have a calm aesthetic (remember the person receiving is grieving) emphasis on luxury as we are looking to attract high end clients so not generic and something that is easily purchased from crafto
Nice to have
• need the following design scheme as it relates to color and font Primary Color Palette: 1. Ecru Stone (Soft Beige/Taupe) – #D7CCC0 • Evokes warmth, trust, and sophistication. 2. Slate Charcoal (Deep Neutral Gray) – #4A4A4A • Represents professionalism, authority, and reliability. Accent Colors: 3. Soft Gold (Understated Elegance) – #C2B280 • Adds a subtle richness without being flashy. 4. Powder White (Clean Background Base) – #FAF9F6 • Used for breathing room, high readability, and elegance. Typography/Callout Highlight Color: 5. Trust Blue (Soft Navy) – #3F4A5F • Often used for headers or key points to add credibility and depth. Tessa Varden should be in cursive, readable and absolutely beautiful
Should not have
• No yellow, do not use ai on my image,

```html
<!DOCTYPE html>
<html lang="en">
<head>
<meta charset="utf-8">
<title>Certified Probate &amp; Trust Postcard</title>
<link rel="stylesheet" href="https://fonts.googleapis.com/css2?family=Nunito:ital,wght@0,300;0,400;0,600;0,700;1,300;1,400;1,600&family=Mrs+Saint+Delafield&display=swap">
<style>
  :root {
    --backdrop: #e4e1e0;
    --slate: #3a3d42;
    --gold: #a87a45;
    --gold-light: #d9b27a;
    --brown: #8f5f2f;
    --ivory: #f1e1c6;
    --sand: #f3e3c7;
    --ink: #3b3b3b;
    --white: #ffffff;
    --stamp: #eeeef0;
    --rule: #5a5a5a;
  }
  * { box-sizing: border-box; margin: 0; padding: 0; }
  html, body { width: 1034px; height: 1200px; overflow: hidden; background: var(--backdrop); }
  body { position: relative; font-family: "Nunito", sans-serif; color: var(--ink); }

  .postcard { position: absolute; left: 134px; width: 767px; background: var(--white); box-shadow: 6px 8px 10px rgba(0,0,0,.35); overflow: hidden; }
  .postcard--front { top: 47px; height: 548px; background: var(--slate); }
  .postcard--back { top: 629px; height: 513px; }

  /* front */
  .hero-photo { position: absolute; left: 0; top: 0; width: 767px; height: 435px;
    background: linear-gradient(180deg, #7fa6bd 0%, #a9c2cc 32%, #b9b3a4 50%, #5d5a52 62%, #3f7c92 72%, #2f6f86 100%); }
  .gold-rule { position: absolute; left: 0; top: 435px; width: 767px; height: 7px;
    background: linear-gradient(90deg, #8c5e2e, #e9d2a6 50%, #8c5e2e); }
  .greeting { position: absolute; left: 257px; top: 18px; font-style: italic; font-weight: 300; color: var(--gold); font-size: 37px; line-height: 44px; }
  .greeting__line { position: absolute; left: 91px; top: 34px; width: 335px; height: 1.5px; background: var(--gold); }
  .headline { position: absolute; left: 257px; top: 62px; width: 480px; font-style: italic; font-weight: 400; color: var(--gold); font-size: 37px; line-height: 44.5px; letter-spacing: .2px; }
  .headshot { position: absolute; left: 558px; top: 260px; width: 182px; height: 182px; border-radius: 50%; border: 7px solid var(--ivory);
    background: radial-gradient(circle at 50% 45%, #8a5a3c 0%, #5a3a2a 45%, #eeeeee 46%, #e6e6e6 100%); }
  .tagline { position: absolute; left: 13px; top: 462px; color: var(--white); }
  .tagline__title { font-weight: 600; font-size: 21px; line-height: 26px; }
  .tagline__sub { font-weight: 300; font-size: 21.5px; line-height: 30px; }
  .tagline__sub b { font-weight: 700; }
  .signature { position: absolute; left: 572px; top: 432px; font-family: "Mrs Saint Delafield", cursive; color: var(--ivory); font-size: 52px; line-height: 60px; white-space: nowrap; }

  /* back */
  .quote-box { position: absolute; left: 0; top: 0; width: 394px; height: 74px; }
  .quote-box svg { position: absolute; inset: 0; }
  .quote-text { position: absolute; left: 48px; top: 14px; width: 330px; font-style: italic; font-weight: 400; color: var(--ivory); font-size: 14px; line-height: 17px; }
  .quote-mark { position: absolute; font-family: Georgia, serif; font-weight: 700; font-style: italic; color: var(--ivory); font-size: 40px; line-height: 40px; }
  .quote-mark--open { left: 22px; top: 5px; }
  .quote-mark--close { left: 144px; top: 45px; }

  .story { position: absolute; left: 0; top: 79px; width: 394px; height: 372px; background: var(--sand); padding: 7px 8px 0 11px; font-size: 11.6px; line-height: 16px; font-weight: 400; }
  .story p { margin-bottom: 7px; }
  .story .highlight { color: var(--brown); font-weight: 600; }
  .story h3 { color: var(--brown); font-weight: 700; font-size: 11px; letter-spacing: .1px; margin: 2px 0 6px; }
  .offers { list-style: none; margin-bottom: 6px; }
  .offers li { position: relative; padding-left: 24px; margin-bottom: 2px; }
  .offers li::before { content: ""; position: absolute; left: 9px; top: 6px; width: 4px; height: 4px; border-radius: 50%; background: var(--brown); }
  .story .closing { font-style: italic; font-weight: 600; color: var(--brown); }

  .cta { position: absolute; left: 0; top: 457px; width: 396px; height: 46px; }
  .cta svg { position: absolute; inset: 0; }
  .cta__text { position: absolute; left: 29px; top: 7px; color: var(--white); font-weight: 600; font-size: 13.4px; line-height: 16px; }

  .divider { position: absolute; left: 400px; top: 0; width: 1px; height: 513px; background: var(--brown); }
  .socials { position: absolute; left: 406px; top: 16px; list-style: none; font-size: 13px; line-height: 19.5px; color: var(--slate); font-weight: 600; }
  .socials li { display: flex; align-items: center; gap: 7px; }
  .socials .dot { width: 13px; height: 13px; background: var(--gold-light); }
  .stamp-box { position: absolute; left: 629px; top: 11px; width: 127px; height: 106px; background: var(--stamp); }
  .address-lines { position: absolute; left: 426px; top: 331px; width: 297px; }
  .address-lines span { display: block; height: 1px; background: var(--rule); margin-bottom: 31px; }
</style>
</head>
<body>

<section class="postcard postcard--front">
  <div class="hero-photo" role="img" aria-label="Photo of the Bay Bridge leading toward the San Francisco skyline across the bay"></div>
  <div class="gold-rule"></div>
  <div class="greeting">Dear:</div>
  <div class="greeting__line" style="left:348px;top:53px;"></div>
  <h1 class="headline">You’ve Taken On So Much – Let Me Help With What Comes Next</h1>
  <div class="headshot" role="img" aria-label="Headshot of Tessa Varden"></div>
  <div class="tagline">
    <p class="tagline__title">Strategic Real Estate Guidance for Probate &amp; Trust</p>
    <p class="tagline__sub">Certified Probate &amp; Trust Specialist <b>|</b> Serving the San Francisco Bay Area</p>
  </div>
  <div class="signature">Tessa Varden</div>
</section>

<section class="postcard postcard--back">
  <div class="quote-box">
    <svg width="394" height="74" viewBox="0 0 394 74">
      <defs>
        <linearGradient id="goldSweep" x1="0" y1="0" x2="1" y2="1">
          <stop offset="0" stop-color="#8c5e2e"/><stop offset=".55" stop-color="#e9d2a6"/><stop offset="1" stop-color="#8c5e2e"/>
        </linearGradient>
      </defs>
      <rect width="394" height="74" fill="#3a3d42"/>
      <polygon points="0,0 28,0 0,56" fill="url(#goldSweep)"/>
      <polygon points="394,26 394,74 364,74" fill="url(#goldSweep)"/>
    </svg>
    <span class="quote-mark quote-mark--open">“</span>
    <p class="quote-text">I lost both of my parents in 2020 – just weeks apart. That experience shaped how I serve every estate I touch.</p>
    <span class="quote-mark quote-mark--close">”</span>
  </div>

  <div class="story">
    <p><span class="highlight">My name is Tessa Varden</span>, and <span class="highlight">I’m a Certified Probate &amp; Trust Specialist</span> who works with families, attorneys, and fiduciaries to guide the real estate side of probate with structure, sensitivity, and strategy.</p>
    <p>Whether you’re navigating this with legal support or filing in pro per, this process is layered – emotional, procedural, and often overwhelming. I provide a steady hand when everything else feels uncertain.</p>
    <p>With over a decade of experience supporting executives at Corvane, Lumirel, and Dunmore Pike, I bring the same operational precision and discretion to every estate I manage. But I also bring empathy – because I’ve been in your shoes.</p>
    <h3>WHAT I OFFER – AT NO UPFRONT COST TO THE ESTATE</h3>
    <ul class="offers">
      <li>Property clean-outs, inspections, and basic preparation<br>– coordinated and covered</li>
      <li>Real estate strategy aligned with court timelines and estate goals</li>
      <li>Hands-on collaboration with attorneys or step-by-step guidance for independent petitioners</li>
      <li>Thoughtful communication that honors your time and your grief</li>
    </ul>
    <p class="closing">Because real estate isn’t just business. For you, it’s personal. For me, it’s both.</p>
  </div>

  <div class="cta">
    <svg width="396" height="46" viewBox="0 0 396 46">
      <polygon points="0,0 396,0 386,23 396,46 0,46" fill="#a87a45"/>
      <polygon points="0,0 388,0 378,22 388,42 0,42" fill="#3a3d42"/>
    </svg>
    <p class="cta__text">If you’re managing a probate or trust estate and need<br>support you can trust – let’s make this easier, together.</p>
  </div>

  <div class="divider"></div>
  <ul class="socials">
    <li><span class="dot"></span>@itstessavoo</li>
    <li><span class="dot"></span>profilehub.net/in/tessahomesagent</li>
  </ul>
  <div class="stamp-box" aria-label="Stamp area"></div>
  <div class="address-lines"><span></span><span></span><span></span><span></span><span></span></div>
</section>

</body>
</html>
```